Page hosted on godaddy.com, Website domain is dalworth4kiva.com

Page should be based on design of my campaign flyer. I will put all text inside pages, they can be layout with top navigation and bottom header that contains contact information. Pages should be white background

I will use html to edit, or I can also get an editor if you specify which one your design is compatible with

Items listed below that are underlined are actual HTML pages
Total number of pages (including BLOG) = 18

Site Structure

HOME
Blog – should be a wordpress blog inside this page
KIVA Board
• Why I am running
• About Me
• How to vote
Automotive
• My Automotive Career
• Automotive for Fun
• Specialty car brokerage
Aviation
• Aviation Experience
• My Favorite Aviation Projects
• Aviation Sales Business
Other Experience
• My Complete Timeline
• Entrepreneurial Activities
• Dalworth Orchard
• Commercial Development
• Home Construction
• Education
Photos
Updates

update, I would ideally like to use wordpress for the site design.

```html
<!DOCTYPE html>
<html lang="en">
<head>
<meta charset="utf-8">
<title>Dalworth for KIVA</title>
<link href="https://fonts.googleapis.com/css2?family=Montserrat:wght@400;500;600&family=Orbitron:wght@700;800;900&display=swap" rel="stylesheet">
<style>
:root{
  --red:#c0181f;
  --dark:#555555;
  --ink:#1e1e1e;
  --panel:#f2f0f0;
  --head:#f0f0f0;
  --black:#000;
  --white:#fff;
}
*{box-sizing:border-box;margin:0;padding:0}
html,body{width:1200px;height:2613px;overflow:hidden;background:var(--white)}
body{font-family:'Montserrat',sans-serif;color:var(--ink);position:relative}
.display{font-family:'Orbitron',sans-serif;font-weight:800;text-transform:uppercase;letter-spacing:.5px}
.abs{position:absolute}

/* header */
.site-header{position:absolute;left:0;top:0;width:1200px;height:130px;background:var(--head)}
.brand{position:absolute;left:112px;top:38px;display:flex;align-items:center;gap:10px;font-weight:600;font-size:24px;color:var(--red)}
.brand-dot{width:18px;height:18px;border-radius:50%;background:var(--red)}
.ad-banner{position:absolute;left:544px;top:23px;width:544px;height:77px;background:linear-gradient(90deg,#7d7f80 0%,#5c5d5e 38%,#4a4a4a 42%,#4a4a4a 100%)}
.ad-banner .ad-photo{position:absolute;left:0;top:0;width:222px;height:77px;background:linear-gradient(180deg,#9aa2a8,#5f6366 60%,#3e3f40)}
.ad-banner h4{position:absolute;left:249px;top:13px;color:var(--white);font-size:12px}
.ad-banner p{position:absolute;left:249px;top:35px;width:275px;color:#ddd;font-size:8.5px;line-height:14px}

/* nav */
.main-nav{position:absolute;left:0;top:130px;width:1200px;height:61px;background:var(--dark);border-bottom:4px solid var(--red)}
.main-nav ul{list-style:none;display:flex;position:absolute;left:110px;top:0;height:57px}
.main-nav li{color:var(--white);font-size:16px;padding:0 25px;display:flex;align-items:center;border-right:1px solid #6c6c6c}
.main-nav li.active{background:var(--red);margin-top:-7px;padding:7px 14px 0;border-right:none;border-radius:3px 3px 0 0}
.search-icon{position:absolute;left:1073px;top:20px}

/* hero */
.hero{position:absolute;left:112px;top:217px;width:627px;height:410px;background:radial-gradient(circle at 55% 35%,#b12126 0%,#6e1216 45%,#2a0b0c 100%)}
.hero .shade{position:absolute;left:0;bottom:0;width:100%;height:190px;background:linear-gradient(180deg,rgba(0,0,0,0),rgba(0,0,0,.55))}
.tag{position:absolute;background:var(--red);color:var(--white);font-family:'Orbitron',sans-serif;font-weight:800;font-size:10px;padding:0 14px;line-height:30px}
.hero .tag{left:18px;top:238px}
.hero h2{position:absolute;left:25px;top:280px;color:var(--white);font-size:19px}
.hero .date{position:absolute;left:25px;top:313px;color:var(--white);font-size:15px;display:flex;align-items:center;gap:6px}
.hero p{position:absolute;left:25px;top:341px;width:590px;color:var(--white);font-size:15.5px;line-height:25px}
.slider-bars{position:absolute;left:112px;top:631px;width:627px;height:6px;display:flex;gap:4px}
.slider-bars span{flex:1;background:var(--dark)}
.slider-bars span:first-child{background:var(--red)}

/* sections */
.section-title{position:absolute;left:112px;color:var(--red);font-size:30px;font-weight:900}
.post{position:absolute;left:112px;width:627px;height:199px;background:var(--panel)}
.post .thumb{position:absolute;left:0;top:0;width:202px;height:199px}
.post h3{position:absolute;left:244px;top:31px;font-size:15px;font-weight:800}
.post .meta{position:absolute;left:248px;top:62px;display:flex;gap:24px;color:var(--red);font-size:15.5px}
.post .meta span{display:flex;align-items:center;gap:8px}
.post p{position:absolute;left:244px;top:94px;width:352px;font-size:15.5px;line-height:25px;text-align:justify;text-align-last:justify;height:75px;overflow:hidden}

/* sidebar */
.widget-head{position:absolute;left:764px;width:324px;height:47px;background:var(--red);color:var(--white);font-size:19px;text-align:center;line-height:48px;font-weight:900}
.widget-body{position:absolute;left:764px;width:324px;background:var(--panel)}
.cat-list{list-style:none;padding:20px 0 0 26px}
.cat-list li{font-size:17px;height:43px;display:flex;align-items:center;gap:10px}
.side-item{position:absolute;display:flex;gap:17px}
.side-item .thumb{width:95px;height:99px;flex:none}
.side-item h5{font-size:14px;line-height:20px;font-weight:800;margin-top:14px}
.side-item .date{color:var(--red);font-size:14px;display:flex;align-items:center;gap:6px;margin-top:5px}
.socials{display:grid;grid-template-columns:repeat(4,47px);gap:16px 32px;padding:16px 0 0 18px}
.socials span{width:47px;height:47px;background:var(--panel);box-shadow:0 0 0 1px #ebe8e8;display:flex;align-items:center;justify-content:center}
.socials i{width:14px;height:14px;border-radius:50%;background:var(--red);display:block}
.gallery{display:grid;grid-template-columns:repeat(4,68px);gap:6px 6px;padding:14px 0 0 16px}
.gallery span{height:72px;display:block}

/* footer */
.site-footer{position:absolute;left:0;top:2203px;width:1200px;height:410px;background:var(--black);color:var(--white)}
.footer-brand{position:absolute;left:0;width:1200px;top:92px;text-align:center;font-size:34px;font-weight:600;display:flex;justify-content:center;align-items:center;gap:14px}
.footer-brand .brand-dot{width:26px;height:26px}
.contact{position:absolute;top:215px;display:flex;align-items:center;gap:17px;font-size:16px;line-height:24px}
.contact .ico{width:40px;height:40px;border-radius:50%;background:var(--red);display:flex;align-items:center;justify-content:center;flex:none}
.footer-links{position:absolute;top:292px;left:0;width:1200px;display:flex;justify-content:center;font-size:16.5px}
.footer-links span{padding:0 20px}
.footer-links b{font-weight:400}
.footer-rule{position:absolute;left:112px;top:340px;width:976px;height:1px;background:#555}
.copyright{position:absolute;top:362px;left:0;width:1200px;text-align:center;font-size:15px}
</style>
</head>
<body>

<svg width="0" height="0" style="position:absolute">
  <defs>
    <symbol id="clock" viewBox="0 0 14 14"><circle cx="7" cy="7" r="5.5" fill="none" stroke="currentColor" stroke-width="2"/><path d="M7 4v3.5h2.5" fill="none" stroke="currentColor" stroke-width="1.6"/></symbol>
    <symbol id="user" viewBox="0 0 14 14"><circle cx="7" cy="4" r="3" fill="currentColor"/><path d="M1 14c0-4 3-6 6-6s6 2 6 6z" fill="currentColor"/></symbol>
    <symbol id="chev" viewBox="0 0 12 12"><path d="M2 2l4 4-4 4M6 2l4 4-4 4" fill="none" stroke="#c0181f" stroke-width="1.6"/></symbol>
  </defs>
</svg>

<header class="site-header">
  <div class="brand"><span class="brand-dot"></span>Dalworth for KIVA</div>
  <div class="ad-banner">
    <div class="ad-photo" role="img" aria-label="Drag strip race car at the starting line"></div>
    <h4 class="display">Lorem ipsum dolor</h4>
    <p>Lorem ipsum dolor sit amet, consectetur adipiscing elit, sed do eiusmod tempor incididunt ut labore et dolore</p>
  </div>
</header>

<nav class="main-nav">
  <ul>
    <li class="active">Home</li><li>KIVA Board</li><li>Automotive</li><li>Aviation</li><li>Other Experience</li><li>Photos</li>
  </ul>
  <svg class="search-icon" width="16" height="16" viewBox="0 0 16 16"><circle cx="6.5" cy="6.5" r="4.8" fill="none" stroke="#fff" stroke-width="2.2"/><path d="M10 10l4.5 4.5" stroke="#fff" stroke-width="2.6"/></svg>
</nav>

<section class="hero" role="img" aria-label="Candidate speaking at a podium on a red-lit stage">
  <div class="shade"></div>
  <span class="tag">KIVA Board</span>
  <h2 class="display">Why I am running</h2>
  <div class="date"><svg width="14" height="14"><use href="#clock"/></svg>April 05,2022</div>
  <p>Lorem ipsum dolor sit amet, consectetur adipiscing elit, sed do eiusmod tempor incididunt ut labore et dolore magna aliqua. Ut enim ad minim</p>
</section>
<div class="slider-bars"><span></span><span></span><span></span></div>

<h2 class="section-title display" style="top:670px">Automotive</h2>

<article class="post" style="top:737px">
  <div class="thumb" role="img" aria-label="Car engine bay" style="background:linear-gradient(135deg,#8a8d8f,#3c3f42 55%,#6d7072)"></div>
  <h3 class="display">My Automotive Career</h3>
  <div class="meta"><span><svg width="13" height="13"><use href="#user"/></svg>Lorem ipsum</span><span><svg width="14" height="14"><use href="#clock"/></svg>April 05 , 2022</span></div>
  <p>Lorem ipsum dolor sit amet, consectetur tempor incididunt ut labore et dolore magna aliqua. Ut enim ad minim veniam, quis</p>
</article>
<article class="post" style="top:953px">
  <div class="thumb" role="img" aria-label="Drag strip with grandstands under a cloudy sky" style="background:linear-gradient(180deg,#a9c3dc,#dfe6ec 40%,#6d7276 60%,#3d3f41)"></div>
  <h3 class="display">Automotive for Fun</h3>
  <div class="meta"><span><svg width="13" height="13"><use href="#user"/></svg>Lorem ipsum</span><span><svg width="14" height="14"><use href="#clock"/></svg>April 05 , 2022</span></div>
  <p>Lorem ipsum dolor sit amet, consectetur tempor incididunt ut labore et dolore magna aliqua. Ut enim ad minim veniam, quis</p>
</article>
<article class="post" style="top:1169px">
  <div class="thumb" role="img" aria-label="Crowd gathered around a car at an auction" style="background:linear-gradient(180deg,#6b6538,#2e2c22 45%,#1f2326)"></div>
  <h3 class="display">Specialty Car Brokerage</h3>
  <div class="meta"><span><svg width="13" height="13"><use href="#user"/></svg>Lorem ipsum</span><span><svg width="14" height="14"><use href="#clock"/></svg>April 05 , 2022</span></div>
  <p>Lorem ipsum dolor sit amet, consectetur tempor incididunt ut labore et dolore magna aliqua. Ut enim ad minim veniam, quis</p>
</article>

<h2 class="section-title display" style="top:1426px">Other Experience</h2>

<article class="post" style="top:1493px">
  <div class="thumb" role="img" aria-label="Board members seated at a meeting" style="background:linear-gradient(135deg,#6a645d,#2b2a2a 50%,#55504c)"></div>
  <h3 class="display">My Complete Timeline</h3>
  <div class="meta"><span><svg width="13" height="13"><use href="#user"/></svg>Lorem ipsum</span><span><svg width="14" height="14"><use href="#clock"/></svg>April 05 , 2022</span></div>
  <p>Lorem ipsum dolor sit amet, consectetur tempor incididunt ut labore et dolore magna aliqua. Ut enim ad minim veniam, quis</p>
</article>
<article class="post" style="top:1710px">
  <div class="thumb" role="img" aria-label="Audience at a conference presentation" style="background:linear-gradient(160deg,#9aa59a,#3a3b3d 45%,#c9c3a5 70%,#23262a)"></div>
  <h3 class="display">Entrepreneurial Activities</h3>
  <div class="meta"><span><svg width="13" height="13"><use href="#user"/></svg>Lorem ipsum</span><span><svg width="14" height="14"><use href="#clock"/></svg>April 05 , 2022</span></div>
  <p>Lorem ipsum dolor sit amet, consectetur tempor incididunt ut labore et dolore magna aliqua. Ut enim ad minim veniam, quis</p>
</article>
<article class="post" style="top:1926px">
  <div class="thumb" role="img" aria-label="Snowy mountain peaks" style="background:linear-gradient(180deg,#4f79a8,#8ea6be 35%,#5d6063 65%,#d8dadb)"></div>
  <h3 class="display">Dalworth Orchard</h3>
  <div class="meta"><span><svg width="13" height="13"><use href="#user"/></svg>Lorem ipsum</span><span><svg width="14" height="14"><use href="#clock"/></svg>April 05 , 2022</span></div>
  <p>Lorem ipsum dolor sit amet, consectetur tempor incididunt ut labore et dolore magna aliqua. Ut enim ad minim veniam, quis</p>
</article>

<!-- sidebar -->
<h3 class="widget-head display" style="top:217px">Category</h3>
<div class="widget-body" style="top:264px;height:363px">
  <ul class="cat-list">
    <li><svg width="12" height="12"><use href="#chev"/></svg>KIVA Board</li>
    <li><svg width="12" height="12"><use href="#chev"/></svg>Automotive</li>
    <li><svg width="12" height="12"><use href="#chev"/></svg>Aviation</li>
    <li><svg width="12" height="12"><use href="#chev"/></svg>Other Experience</li>
    <li><svg width="12" height="12"><use href="#chev"/></svg>Photos</li>
  </ul>
</div>

<h3 class="widget-head display" style="top:641px">Aviation</h3>
<div class="widget-body" style="top:688px;height:397px"></div>
<div class="side-item" style="left:807px;top:713px">
  <div class="thumb" role="img" aria-label="Pilot in a small aircraft cockpit" style="background:linear-gradient(135deg,#b7b2a6,#4c4a45)"></div>
  <div><h5 class="display">Aviation<br>Experience</h5><div class="date"><svg width="13" height="13"><use href="#clock"/></svg>April 05 ,2022</div></div>
</div>
<div class="side-item" style="left:807px;top:830px">
  <div class="thumb" role="img" aria-label="Twin-engine plane in flight" style="background:linear-gradient(180deg,#8fa2b0,#6d7e6a)"></div>
  <div><h5 class="display">My Favorite<br>Aviation<br>Projects</h5><div class="date"><svg width="13" height="13"><use href="#clock"/></svg>April 05 ,2022</div></div>
</div>
<div class="side-item" style="left:807px;top:946px">
  <div class="thumb" role="img" aria-label="Private jet on a runway" style="background:linear-gradient(180deg,#2f6fc0,#8db6e0 55%,#7d7c76)"></div>
  <div><h5 class="display">Aviation Sale<br>Business</h5><div class="date"><svg width="13" height="13"><use href="#clock"/></svg>April 05 ,2022</div></div>
</div>

<h3 class="widget-head display" style="top:1102px">Soical Media</h3>
<div class="widget-body" style="top:1149px;height:170px">
  <div class="socials">
    <span><i></i></span><span><i></i></span><span><i></i></span><span><i></i></span>
    <span><i></i></span><span><i></i></span><span><i></i></span>
    <span><svg width="22" height="16" viewBox="0 0 22 16"><rect width="22" height="16" rx="1.5" fill="#c0181f"/><path d="M1 1.5l10 7.5 10-7.5" fill="none" stroke="#f2f0f0" stroke-width="1.8"/></svg></span>
  </div>
</div>

<h3 class="widget-head display" style="top:1324px">Feed Back</h3>
<div class="side-item" style="left:764px;top:1444px">
  <div class="thumb" role="img" aria-label="Couple in an empty commercial space" style="background:linear-gradient(180deg,#e8ecef,#b9c0c5)"></div>
  <div><h5 class="display">Commercial<br>Development</h5><div class="date"><svg width="13" height="13"><use href="#clock"/></svg>April 05 ,2022</div></div>
</div>
<div class="side-item" style="left:764px;top:1561px">
  <div class="thumb" role="img" aria-label="House under construction" style="background:linear-gradient(180deg,#8fb0d2,#c9a77b 60%,#6b5a44)"></div>
  <div><h5 class="display">Home<br>Construction</h5><div class="date"><svg width="13" height="13"><use href="#clock"/></svg>April 05 ,2022</div></div>
</div>
<div class="side-item" style="left:764px;top:1677px">
  <div class="thumb" role="img" aria-label="Open book before a chalkboard" style="background:linear-gradient(180deg,#4f6a4d,#8a8c7d 55%,#e2dcd0)"></div>
  <div><h5 class="display" style="margin-top:26px">Education</h5><div class="date"><svg width="13" height="13"><use href="#clock"/></svg>April 05 ,2022</div></div>
</div>

<h3 class="widget-head display" style="top:1795px;padding-right:36px">Photos</h3>
<div class="widget-body" style="top:1842px;height:284px">
  <div class="gallery">
    <span role="img" aria-label="Black sports car" style="background:linear-gradient(180deg,#7c9a6d,#1e2327)"></span>
    <span role="img" aria-label="Engine parts" style="background:linear-gradient(180deg,#9c9a96,#454443)"></span>
    <span role="img" aria-label="Red car" style="background:linear-gradient(180deg,#6d8a56,#b31c2b)"></span>
    <span role="img" aria-label="Businessmen in an office" style="background:linear-gradient(180deg,#dfe4ea,#3b4048)"></span>
    <span role="img" aria-label="Airliner at sunset" style="background:linear-gradient(180deg,#4a78a8,#e08b47)"></span>
    <span role="img" aria-label="Red sports car" style="background:linear-gradient(180deg,#7c7d7e,#b51d22)"></span>
    <span role="img" aria-label="Construction workers" style="background:linear-gradient(180deg,#9db7d4,#6f6a52)"></span>
    <span role="img" aria-label="Mountain peak" style="background:linear-gradient(180deg,#2f6db4,#c9d3dc)"></span>
    <span role="img" aria-label="Modern house" style="background:linear-gradient(180deg,#a9c6e3,#c2a681)"></span>
    <span role="img" aria-label="Car at an auction" style="background:linear-gradient(180deg,#7a6b2e,#1b2b24)"></span>
    <span role="img" aria-label="Cars on a road" style="background:linear-gradient(180deg,#9fb4c8,#4a4e52)"></span>
    <span role="img" aria-label="Businessman in a city" style="background:linear-gradient(180deg,#20304a,#6f9ac6)"></span>
  </div>
</div>

<footer class="site-footer">
  <div class="footer-brand"><span class="brand-dot"></span>Dalworth for KIVA</div>
  <div class="contact" style="left:169px">
    <span class="ico"><svg width="14" height="18" viewBox="0 0 14 18"><path d="M7 0C3 0 0 3 0 7c0 5 7 11 7 11s7-6 7-11c0-4-3-7-7-7z" fill="#fff"/><circle cx="7" cy="7" r="2.5" fill="#c0181f"/></svg></span>
    <span>2003 Lorem ipsum dolor<br>sit amet62</span>
  </div>
  <div class="contact" style="left:528px">
    <span class="ico"><svg width="16" height="16" viewBox="0 0 16 16"><path d="M3.5 1l3 3.2-1.6 2a9 9 0 004.9 4.9l2-1.6 3.2 3-1.6 2.5C6.8 15.5.5 9.2 1 2.6z" fill="#fff"/></svg></span>
    <span>734 555-0148</span>
  </div>
  <div class="contact" style="left:836px">
    <span class="ico"><svg width="16" height="12" viewBox="0 0 16 12"><rect width="16" height="12" rx="1" fill="#fff"/><path d="M1 1l7 5.5L15 1" fill="none" stroke="#c0181f" stroke-width="1.5"/></svg></span>
    <span>www.dalworth4kiva.com</span>
  </div>
  <div class="footer-links">
    <span>Home</span><b>|</b><span>KIVA Board</span><b>|</b><span>Automotive</span><b>|</b><span>Aviation</span><b>|</b><span>Other Experience</span><b>|</b><span>Photos</span>
  </div>
  <div class="footer-rule"></div>
  <p class="copyright">©Copyrights 2022 dalworth4kiva | All Rights Reserved</p>
</footer>

</body>
</html>
```